Ridgely Forge business card for handing simple contact information and generating service awareness

Utilizing the attached logo(s), generate a professional, but approachable, card conveying a sense of capability and integrity. Please only use one logo of the four attached; the different colors are all acceptable, but preference will be given to a design integrating a teal/turquoise logo,

I do not know where to put in the contact information or details?

Target Market(s)

Agriculture, Farming, Timber, Forestry, Construction, Crane Service

Industry/Entity Type

Contact Information for Business Card

Name, Phone Number, email address

Colors

Designer to choose colors to be used in the design.

Requirements
Nice to have
• It would be great to have either a mountain or one of the attached cranes as a backdrop on the rear of the card. Simple watermarks and/or Debossing is also great

```html
<!DOCTYPE html>
<html lang="en">
<head>
<meta charset="utf-8">
<title>Ridgely Forge – Business Card</title>
<link rel="stylesheet" href="https://fonts.googleapis.com/css2?family=Montserrat:wght@400;700;800&display=swap">
<style>
  :root {
    --backdrop: #e4e4e6;
    --ink: #111111;
    --paper: #fbfbfb;
    --art-light: #f2f2f2;
    --art-mid: #bdbdbd;
    --art-dark: #2b2b2b;
  }
  * { box-sizing: border-box; margin: 0; padding: 0; }
  html, body {
    width: 1200px; height: 900px; overflow: hidden;
    background: var(--backdrop);
    font-family: "Montserrat", sans-serif;
  }
  .stage { position: relative; width: 1200px; height: 900px; }

  .card {
    position: absolute; top: 130px;
    width: 360px; height: 630px;
    border-radius: 4px; overflow: hidden;
    box-shadow: 0 12px 30px rgba(0,0,0,0.2);
  }
  .card--front { left: 190px; background: var(--ink); color: var(--paper); }
  .card--back  { left: 650px; background: var(--paper); color: var(--ink); }

  .brand-name {
    font-weight: 800; text-transform: uppercase;
    letter-spacing: 0.03em; line-height: 1; font-size: 32px;
  }
  .brand-tagline {
    font-weight: 700; font-size: 14px; letter-spacing: 0.08em;
    text-transform: uppercase; margin-top: 10px;
  }
  .brand-est {
    font-size: 11px; letter-spacing: 0.45em; margin-top: 6px;
  }

  /* front */
  .front-brand { position: absolute; left: 36px; top: 48px; }
  .front-artwork {
    position: absolute; left: -30px; bottom: -30px;
    width: 420px; height: 440px;
  }

  /* back */
  .back-emblem {
    position: absolute; right: 34px; top: 34px;
    width: 130px; height: 130px;
  }
  .back-brand { position: absolute; left: 34px; top: 180px; }
  .contact { position: absolute; left: 34px; top: 300px; }
  .contact__name { font-weight: 700; font-size: 36px; line-height: 1.05; }
  .contact__title { font-size: 16px; margin-top: 6px; }
  .contact__rule { width: 130px; height: 4px; background: var(--ink); margin: 10px 0 14px; }
  .contact__line { font-size: 15.5px; line-height: 1.5; }
  .contact__line--address { margin-top: 2px; }
</style>
</head>
<body>
<div class="stage">
  <section class="card card--front">
    <div class="front-brand">
      <p class="brand-name">Ridgely Forge</p>
      <p class="brand-tagline">Timber and Tractors</p>
      <p class="brand-est">— EST. 2024 —</p>
    </div>
    <svg class="front-artwork" viewBox="0 0 420 440" role="img" aria-label="Large emblem artwork: mountain, pine forest and tractor scene in white on black">
      <defs>
        <radialGradient id="artTone" cx="40%" cy="55%" r="60%">
          <stop offset="0%" stop-color="var(--art-light)"/>
          <stop offset="100%" stop-color="var(--art-mid)"/>
        </radialGradient>
      </defs>
      <circle cx="200" cy="240" r="210" fill="url(#artTone)"/>
    </svg>
  </section>

  <section class="card card--back">
    <svg class="back-emblem" viewBox="0 0 130 130" role="img" aria-label="Emblem artwork: mountain, forest and tractor in a circle">
      <circle cx="65" cy="65" r="63" fill="var(--art-dark)"/>
    </svg>
    <div class="back-brand">
      <p class="brand-name">Ridgely Forge</p>
      <p class="brand-tagline">Timber and Tractors</p>
      <p class="brand-est">— EST. 2024 —</p>
    </div>
    <div class="contact">
      <p class="contact__name">YOUR NAME</p>
      <p class="contact__title">Your Tittle Here</p>
      <div class="contact__rule"></div>
      <p class="contact__line">012 345 6789 | Fax 012 345 6789</p>
      <p class="contact__line">Your@ridgelymail.com</p>
      <p class="contact__line">www.ridgelyforge-site.com</p>
      <p class="contact__line contact__line--address">No.000, Your Street, Province,<br>Your Country</p>
    </div>
  </section>
</div>
</body>
</html>
```